Letterhead and Business card for Construction company

We need a letterhead and business card with our new company logo. We are based in NY. We develop and build properties.

The design should incorporate some unique feature from the logo (shape, font...). it should look like an extension from it.

Design should be clean and elegant, professional, not too busy.

The letterhead should include:
Logo (attached)
Address
Phone
Email

Please find the attached logo images and AI file.

Target Market(s)

Construction industry professionals

Industry/Entity Type

Construction, Development

Font styles to use
Sans Serif

Colors

Designer to choose colors to be used in the design.

Requirements
Must have
• Design should incorporate logo elements, additional assets are welcome. I'd like to see some other shapes / images invorporated too.

```html
<!DOCTYPE html>
<html lang="en">
<head>
<meta charset="utf-8">
<title>Kestrel Build — Business Card</title>
<link rel="stylesheet" href="https://fonts.googleapis.com/css2?family=Archivo:wght@600;800&family=Karla:wght@400;500&display=swap">
<style>
  :root{
    --page:#e8e8e8;
    --card:#ffffff;
    --ink:#231f20;
    --text:#3a3a3a;
    --orange:#f2762a;
    --orange-deep:#ec5f17;
    --orange-light:#f69a4a;
    --faint:#f1f1f1;
  }
  *{box-sizing:border-box;margin:0;padding:0}
  html,body{width:1200px;height:1200px;overflow:hidden;background:var(--page)}
  body{position:relative;font-family:"Karla",sans-serif}

  .card{position:absolute;left:262px;width:686px;height:392px;overflow:hidden;
        box-shadow:0 14px 24px rgba(0,0,0,.18)}
  .card--front{top:165px;background:var(--card)}
  .card--back{top:653px;background:linear-gradient(200deg,var(--orange-light) 0%,var(--orange) 45%,var(--orange-deep) 100%)}

  .front__panel{position:absolute;left:410px;top:20px;width:276px;height:332px}

  .wordmark{position:absolute;display:flex;align-items:center;gap:10px;
            font-family:"Archivo",sans-serif;font-weight:800;letter-spacing:.5px;line-height:1}
  .wordmark__square{display:block;background:var(--orange)}
  .front__wordmark{left:62px;top:110px;font-size:34px;color:var(--ink)}
  .front__wordmark .wordmark__square{width:26px;height:26px}

  .contact{position:absolute;left:62px;top:238px;list-style:none;color:var(--text);
           font-size:14.5px;line-height:19px;letter-spacing:.2px}
  .contact li{display:flex;gap:8px;margin-bottom:3px}
  .contact svg{flex:none;width:13px;height:13px;margin-top:3px;fill:var(--orange)}
  .contact span{display:block}

  .person{position:absolute;right:52px;top:244px;text-align:right}
  .person__name{font-family:"Archivo",sans-serif;font-weight:600;font-size:24px;color:var(--ink);letter-spacing:-.2px;line-height:1}
  .person__role{font-size:14.5px;color:var(--orange);letter-spacing:.6px;margin-top:2px}

  .band{position:absolute;left:0;bottom:0;width:686px;height:40px}
  .band__url{position:absolute;left:441px;bottom:10px;color:#fff;font-family:"Karla",sans-serif;
             font-weight:500;font-size:16px;letter-spacing:1.6px}

  .back__wordmark{left:50%;top:50%;transform:translate(-50%,-50%);font-size:48px;color:#fff;gap:14px}
  .back__wordmark .wordmark__square{width:36px;height:36px;background:#fff}
</style>
</head>
<body>
  <section class="card card--front" aria-label="Business card front">
    <svg class="front__panel" role="img" aria-label="Faint decorative background panel" viewBox="0 0 276 332" preserveAspectRatio="none">
      <defs>
        <linearGradient id="panelFade" x1="0" y1="0" x2="1" y2="0">
          <stop offset="0" stop-color="#ececec" stop-opacity=".9"/>
          <stop offset="1" stop-color="#fdeee3" stop-opacity=".9"/>
        </linearGradient>
      </defs>
      <rect x="0" y="0" width="276" height="332" fill="url(#panelFade)"/>
    </svg>

    <div class="wordmark front__wordmark">
      <span class="wordmark__square"></span>
      <span class="wordmark__name">KESTREL BUILD</span>
    </div>

    <ul class="contact">
      <li>
        <svg viewBox="0 0 24 24"><path d="M12 2a7 7 0 0 0-7 7c0 5.2 7 13 7 13s7-7.8 7-13a7 7 0 0 0-7-7zm0 9.5A2.5 2.5 0 1 1 12 6.5a2.5 2.5 0 0 1 0 5z"/></svg>
        <div><span>2140 Harbor View Road</span><span>Albany, New York 12207</span></div>
      </li>
      <li>
        <svg viewBox="0 0 24 24"><path d="M6.6 10.8a15.1 15.1 0 0 0 6.6 6.6l2.2-2.2a1 1 0 0 1 1-.25 11.4 11.4 0 0 0 3.6.57 1 1 0 0 1 1 1V20a1 1 0 0 1-1 1A17 17 0 0 1 3 4a1 1 0 0 1 1-1h3.5a1 1 0 0 1 1 1c0 1.25.2 2.45.57 3.57a1 1 0 0 1-.25 1z"/></svg>
        <span>518-304-7721</span>
      </li>
      <li>
        <svg viewBox="0 0 24 24"><path d="M2 5h20v14H2zm2 2v.5l8 5 8-5V7z"/></svg>
        <span>info@kestrelbuild.com</span>
      </li>
    </ul>

    <div class="person">
      <p class="person__name">DANIEL REYES</p>
      <p class="person__role">President</p>
    </div>

    <svg class="band" viewBox="0 0 686 40" aria-hidden="true">
      <polygon points="0,0 360,0 366,-4 398,-4 412,40 0,40" fill="var(--ink)"/>
      <polygon points="410,-4 686,-4 686,40 425,40" fill="var(--orange)"/>
    </svg>
    <p class="band__url">KESTRELBUILD.COM</p>
  </section>

  <section class="card card--back" aria-label="Business card back">
    <div class="wordmark back__wordmark">
      <span class="wordmark__square"></span>
      <span class="wordmark__name">KESTREL BUILD</span>
    </div>
  </section>
</body>
</html>
```